Copperleaf Motorized Shade Business Card

Hello, we've had our logo made. Now we are looking for a clean and cool looking business card. One side can just be the logo with any design elements that might look good with it. The other side will be Name, Phone Number and Email. There will not be an address on the card.

```html
<!DOCTYPE html>
<html lang="en">
<head>
<meta charset="utf-8">
<title>Copperleaf Motorized Shade – Business Card</title>
<link rel="stylesheet" href="https://fonts.googleapis.com/css2?family=Poppins:wght@500;600;700&display=swap">
<style>
  :root {
    --navy: #0b3a74;
    --sky: #0aa9e6;
    --sun: #fbbf1a;
    --slate: #6f8fb8;
    --paper: #ffffff;
    --paper-shade: #eceef1;
    --backdrop: #a3a3a3;
  }
  html, body {
    margin: 0;
    padding: 0;
    width: 738px;
    height: 1200px;
    overflow: hidden;
    background: var(--backdrop);
    font-family: "Poppins", sans-serif;
  }
  .canvas {
    width: 738px;
    height: 1200px;
    display: flex;
    flex-direction: column;
    align-items: center;
    justify-content: center;
    gap: 50px;
  }
  .card {
    width: 640px;
    height: 365px;
    display: block;
    border-radius: 12px;
    box-shadow: 0 10px 22px rgba(0,0,0,0.28);
  }
  .fill-navy { fill: var(--navy); }
  .fill-sky { fill: var(--sky); }
  .fill-sun { fill: var(--sun); }
  .fill-slate { fill: var(--slate); }
  .fill-paper { fill: var(--paper); }
  .brand-name { font-family: "Poppins", sans-serif; font-weight: 700; fill: var(--navy); }
  .web-link { font-family: "Poppins", sans-serif; font-weight: 500; fill: var(--paper); font-size: 11.5px; }
  .contact-text { font-family: "Poppins", sans-serif; font-weight: 500; fill: var(--paper); font-size: 9px; }
  .contact-name { font-family: "Poppins", sans-serif; font-weight: 600; fill: var(--paper); font-size: 11px; }
  .icon-line { fill: none; stroke: var(--paper); stroke-width: 1.1; stroke-linecap: round; stroke-linejoin: round; }
</style>
</head>
<body>
<main class="canvas">

  <svg class="card card-front" viewBox="0 0 540 308" aria-label="Business card front">
    <defs>
      <linearGradient id="paperGrad" x1="0" y1="0" x2="1" y2="1">
        <stop offset="0" stop-color="var(--paper-shade)"/>
        <stop offset="0.5" stop-color="var(--paper)"/>
        <stop offset="1" stop-color="var(--paper-shade)"/>
      </linearGradient>
      <clipPath id="frontClip"><rect width="540" height="308" rx="10"/></clipPath>
    </defs>
    <g clip-path="url(#frontClip)">
      <rect class="card-paper" width="540" height="308" fill="url(#paperGrad)"/>
      <polygon class="fill-navy corner-tab" points="0,0 26,0 0,44"/>
      <polygon class="fill-navy side-panel" points="435,14 540,14 540,308 287,308"/>
      <polygon class="fill-sun accent-chip" points="530,18 540,18 540,46 518,46"/>

      <polygon class="fill-sky web-band" points="0,240 262,240 246,298 0,298"/>
      <polygon class="fill-sun stripe" points="275,240 305,240 288,298 258,298"/>
      <polygon class="fill-sky stripe" points="312,240 456,240 430,298 292,298"/>
      <polygon class="fill-sun stripe" points="480,240 508,240 482,298 454,298"/>
      <polygon class="fill-paper stripe" points="526,240 540,240 540,298 500,298"/>
      <text class="web-link" x="30" y="273">www.copperleafshades.com</text>

      <rect class="fill-sky brand-mark" x="55" y="46" width="22" height="22"/>
      <text class="brand-name" x="62" y="168" font-size="40">COPPERLEAF</text>
      <text class="brand-name" x="64" y="198" font-size="14" letter-spacing="3">MOTORIZED SHADE</text>
    </g>
  </svg>

  <svg class="card card-back" viewBox="0 0 540 308" aria-label="Business card back">
    <defs>
      <clipPath id="backClip"><rect width="540" height="308" rx="10"/></clipPath>
    </defs>
    <g clip-path="url(#backClip)">
      <rect class="card-paper" width="540" height="308" fill="url(#paperGrad)"/>
      <polygon class="fill-navy side-panel" points="425,0 540,0 540,308 330,308 380,125"/>
      <rect class="fill-navy base-panel" x="0" y="225" width="540" height="83"/>
      <polygon class="fill-navy stripe" points="370,15 397,15 365,95 340,95"/>
      <polygon class="fill-sky contact-band" points="0,125 498,125 455,212 0,212"/>
      <polygon class="fill-paper stripe" points="510,120 540,120 510,210 480,210"/>
      <polygon class="fill-paper divider" points="83,225 87,225 49,308 45,308"/>
      <polygon class="fill-slate panel" points="92,225 282,225 246,308 54,308"/>
      <polygon class="fill-paper divider" points="287,225 291,225 255,308 251,308"/>
      <polygon class="fill-sun stripe" points="330,228 362,228 328,300 296,300"/>
      <polygon class="fill-sun stripe" points="372,228 404,228 370,300 338,300"/>
      <polygon class="fill-sun stripe" points="414,228 430,228 396,300 380,300"/>
      <polygon class="fill-sun stripe" points="512,290 540,290 540,308 504,308"/>

      <rect class="fill-sky brand-mark" x="36" y="18" width="14" height="14"/>
      <text class="brand-name" x="38" y="82" font-size="26">COPPERLEAF</text>
      <text class="brand-name" x="39" y="102" font-size="10" letter-spacing="2">MOTORIZED SHADE</text>

      <g class="contact-left">
        <text class="contact-name" x="38" y="152">Daniel Whitmore</text>
        <rect class="icon-line mail-icon" x="38" y="175" width="10" height="7"/>
        <path class="icon-line" d="M38,175 l5,4 l5,-4"/>
        <text class="contact-text" x="56" y="182">hello@copperleafshades.com</text>
      </g>
      <rect class="fill-paper col-rule" x="254" y="133" width="0.8" height="70"/>
      <g class="contact-right">
        <path class="icon-line phone-icon" d="M262,139 l3,-1 l2,4 l-2,1.5 a8,8 0 0 0 3.5,3.5 l1.5,-2 l4,2 l-1,3 a10,10 0 0 1 -11,-11z"/>
        <text class="contact-text" x="282" y="146">555-014-2231</text>
        <path class="icon-line phone-icon" d="M262,153 l3,-1 l2,4 l-2,1.5 a8,8 0 0 0 3.5,3.5 l1.5,-2 l4,2 l-1,3 a10,10 0 0 1 -11,-11z"/>
        <text class="contact-text" x="282" y="161">555-019-7784</text>
        <circle class="icon-line globe-icon" cx="267" cy="179" r="5"/>
        <path class="icon-line" d="M262,179 h10 M267,174 c-3,3 -3,7 0,10 c3,-3 3,-7 0,-10"/>
        <text class="contact-text" x="282" y="182">www.copperleafshades.com</text>
      </g>
    </g>
  </svg>

</main>
</body>
</html>
```